Artisan Bread Company needs a business card

I need a business card design, for an artisan bread company called "Holloway's Bread".

I would like the logo on one side, and on the other, I would like it to say

Dorian Holloway
Baker
416.552.0193
hollowaysbread@breadmail.example

Not necessarily in that order- but it must have these.

Industry/Entity Type

Business

Font styles to use
Serif

Requirements
Must have
• The provided logo on the front, this on the back-
• Dorian Holloway
• Baker
• 416.552.0193
• hollowaysbread@breadmail.example

```html
<!DOCTYPE html>
<html lang="en">
<head>
<meta charset="utf-8">
<title>Holloway's Bread – Business Card</title>
<link rel="stylesheet" href="https://fonts.googleapis.com/css2?family=Open+Sans:wght@400;600;700&display=swap">
<style>
  :root {
    --backdrop: #e6e3df;
    --card-dark: #000000;
    --card-light: #ffffff;
    --ink: #1b1b1b;
    --ink-soft: #444444;
    --on-dark: #ffffff;
    --shadow: rgba(0, 0, 0, 0.28);
  }
  * { margin: 0; padding: 0; box-sizing: border-box; }
  html, body {
    width: 1200px;
    height: 649px;
    overflow: hidden;
    background: var(--backdrop);
    font-family: "Open Sans", Arial, sans-serif;
  }
  .canvas { position: relative; width: 1200px; height: 649px; }

  .card {
    position: absolute;
    width: 545px;
    height: 310px;
    box-shadow: 0 6px 14px var(--shadow);
  }

  /* Front: brand side */
  .card--front {
    left: 140px;
    top: 112px;
    background: var(--card-dark);
    color: var(--on-dark);
  }
  .brand-block {
    position: absolute;
    left: 32px;
    top: 178px;
    width: 210px;
  }
  .brand-name {
    font-weight: 600;
    font-size: 27px;
    line-height: 1.2;
    white-space: nowrap;
  }
  .brand-rule {
    height: 1px;
    background: var(--on-dark);
    margin: 12px 0 10px;
  }
  .brand-web {
    font-size: 15px;
    letter-spacing: 1.3px;
    white-space: nowrap;
  }

  /* Back: contact side */
  .card--back {
    left: 546px;
    top: 230px;
    background: var(--card-light);
    color: var(--ink);
  }
  .card--back .brand-name {
    position: absolute;
    right: 36px;
    top: 58px;
    color: var(--ink);
    font-size: 26px;
  }
  .contact {
    position: absolute;
    left: 32px;
    top: 184px;
  }
  .contact-name { font-weight: 700; font-size: 20px; line-height: 1.2; }
  .contact-role { font-size: 15px; color: var(--ink-soft); margin-top: 2px; }
  .contact-list { list-style: none; margin-top: 14px; }
  .contact-item {
    display: flex;
    align-items: center;
    gap: 8px;
    font-size: 14.5px;
    color: var(--ink-soft);
    line-height: 21px;
  }
  .contact-icon { width: 13px; height: 13px; fill: var(--ink); flex: none; }
</style>
</head>
<body>
<main class="canvas">
  <section class="card card--front" aria-label="Business card front">
    <div class="brand-block">
      <p class="brand-name">Holloway's Bread</p>
      <div class="brand-rule"></div>
      <p class="brand-web">www.hollowaysbread.example</p>
    </div>
  </section>

  <section class="card card--back" aria-label="Business card back">
    <p class="brand-name">Holloway's Bread</p>
    <div class="contact">
      <p class="contact-name">Dorian Holloway</p>
      <p class="contact-role">Baker</p>
      <ul class="contact-list">
        <li class="contact-item">
          <svg class="contact-icon" viewBox="0 0 24 24" aria-hidden="true"><path d="M6.6 10.8a15.2 15.2 0 0 0 6.6 6.6l2.2-2.2a1 1 0 0 1 1-.25 11.4 11.4 0 0 0 3.6.57 1 1 0 0 1 1 1V20a1 1 0 0 1-1 1A17 17 0 0 1 3 4a1 1 0 0 1 1-1h3.5a1 1 0 0 1 1 1c0 1.25.2 2.45.57 3.57a1 1 0 0 1-.25 1z"/></svg>
          <span>416.552.0193</span>
        </li>
        <li class="contact-item">
          <svg class="contact-icon" viewBox="0 0 24 24" aria-hidden="true"><path d="M2 5h20v14H2z M2 5l10 7 10-7" fill="none" stroke="currentColor"/><path d="M2 6.5l10 7 10-7V19H2z"/><path d="M2 5h20l-10 7z"/></svg>
          <span>hollowaysbread@breadmail.example</span>
        </li>
      </ul>
    </div>
  </section>
</main>
</body>
</html>
```